Youth organisation needs design work for awards booklet

We are from The Young Pathfinders' Corps in Singapore, and we need design work for an awards booklet for one of our most prestigious awards, the Keystone Honour. The recipients are sixteen year old teenagers. This booklet will comprise of the list of the recipients, congratulatory notes and stories from some of the recipients. This booklet will be printed for each of the recipient and his guests to keep as a remembrance. We are looking for dual or tri-colour scheme, with bronze being one of the colours.
Updates

Target Market(s)

Recipients of the Award, their parents, school Principals and teachers

Requirements
Must have
• We are looking to have around 16 designed pages, including front and back cover. Size of the booklet is:
Closed - W100mm x H210mm; Opened - W200mm x H210mm
Cover page - picture of the Award
Page 3 - programme highlights
Page 4-5 - picture of the Award and description of the Award
Page 6-7 - Testimonials
Page 8-14 - List of recipients (to be provided upon confirmation of designer)
Page 15 - blank page or acknowledgments page
Back Cover - YP Logo and contact details
(Refer to previous years' booklets for reference)

Designers can submit just the cover pages as well as 1 sample inner page to get a sense of the overall style of design during the selection round.
Nice to have
• Clean, prestigious/premium look

```html
<!DOCTYPE html>
<html lang="en">
<head>
<meta charset="utf-8">
<title>Keystone Honour – Program Highlights</title>
<link rel="stylesheet" href="https://fonts.googleapis.com/css2?family=Montserrat:wght@800&family=Outfit:wght@400&display=swap">
<style>
  :root {
    --bg-deep: #141312;
    --bg-mid: #1f1d1b;
    --bronze: #c9b27d;
    --ink: #f4f2ee;
    --badge-light: #d9d4c8;
    --badge-dark: #8c867a;
  }
  html, body {
    margin: 0;
    padding: 0;
    overflow: hidden;
  }
  .spread {
    position: relative;
    width: 1144px;
    height: 1200px;
    overflow: hidden;
    background: radial-gradient(ellipse at 40% 10%, #262422 0%, var(--bg-mid) 35%, var(--bg-deep) 100%);
    font-family: "Outfit", "Helvetica Neue", Arial, sans-serif;
    color: var(--ink);
    font-size: 21px;
    line-height: 29px;
  }
  .award-image {
    position: absolute;
    left: 74px;
    top: 78px;
    width: 196px;
    height: 254px;
  }
  .award-intro {
    position: absolute;
    left: 69px;
    top: 384px;
    width: 420px;
    margin: 0;
  }
  .award-intro p {
    margin: 0 0 28px;
  }
  .requirements {
    position: absolute;
    left: 69px;
    top: 643px;
    width: 420px;
    margin: 0;
    padding: 0;
    list-style: none;
  }
  .requirements li {
    position: relative;
    padding-left: 13px;
  }
  .requirements li::before {
    content: "•";
    position: absolute;
    left: 0;
  }
  .section-title {
    position: absolute;
    left: 636px;
    top: 158px;
    margin: 0;
    font-family: "Montserrat", "Helvetica Neue", Arial, sans-serif;
    font-weight: 800;
    font-size: 56px;
    line-height: 54px;
    letter-spacing: 1px;
  }
  .section-title .accent { color: var(--bronze); display: block; }
  .section-title .main { color: var(--ink); display: block; }
  .programme {
    position: absolute;
    left: 636px;
    top: 365px;
    width: 480px;
    margin: 0;
    padding: 0;
    list-style: none;
  }
  .programme li { margin-bottom: 11px; }
  .programme .time { display: block; color: var(--bronze); margin-bottom: -3px; }
  .programme .name { color: var(--bronze); }
</style>
</head>
<body>
<main class="spread">
  <svg class="award-image" viewBox="0 0 196 254" role="img" aria-label="Photograph of the Keystone Honour medal">
    <defs>
      <radialGradient id="medalTone" cx="40%" cy="35%" r="70%">
        <stop offset="0%" stop-color="var(--badge-light)"/>
        <stop offset="100%" stop-color="var(--badge-dark)"/>
      </radialGradient>
    </defs>
    <rect x="72" y="0" width="52" height="50" rx="6" fill="url(#medalTone)"/>
    <circle cx="98" cy="140" r="96" fill="url(#medalTone)"/>
    <ellipse cx="98" cy="240" rx="20" ry="12" fill="url(#medalTone)"/>
  </svg>

  <div class="award-intro">
    <p>The Award is the highest and most honourable award a Boy can attain in the Seniors Programme.</p>
    <p>Recipients of this award must have satisfied the following requirements:</p>
  </div>

  <ul class="requirements">
    <li>Attained the Senior Proficiency Award, which represents the recipients’ completion of our Core Curriculum,</li>
    <li>Attained Proficiency Awards at the Advanced Level,</li>
    <li>Shown outstanding leadership abilities and character befitting that of a model YP Boy, and</li>
    <li>Recommended by the Company Captain and School.</li>
  </ul>

  <h1 class="section-title"><span class="accent">PROGRAM</span><span class="main">HIGHLIGHTS</span></h1>

  <ul class="programme">
    <li><span class="time">17:00</span>Arrival of Guests &amp; Registration</li>
    <li><span class="time">18:00</span>Arrival of Guest-of-Honour <span class="name">Mr Tan Wei Ming</span><br>Senior Parliamentary Secretary</li>
    <li>Opening item</li>
    <li>Welcome Address by <span class="name">Mr Lim Chee Kong</span><br>Brigade President</li>
    <li>Address by the Guest-of-Honour</li>
    <li>Keystone Honour Presentation</li>
    <li>Commencement of Dinner</li>
    <li>Testimonials &amp; Performance</li>
    <li><span class="time">21:30</span>End of Ceremony</li>
  </ul>
</main>
</body>
</html>
```